Web Design

Hello, I am a guitarist seeking a design for my new website.
Task Outline:
I am looking for a new website design that captures me as an Guitarist/artist. A clean, simple and professional look.
Heading – either dorvelquist.com as the header or ‘The Official website of Teo Varsko’ (Feel free to have a go at a logo for my name as well, either just the initials or full name).
Here are 3 websites that I like -
http://www.pelo.com/
http://www.trabunelo.com.br/
http://www.vanyabortsukov.com/
These are the different pages -
Home/Splash
News
Tours
Bio
Gear
Video
Contact
* I have attached 3 main pics to work around.
Here are some social media links -
Tunevault link - https://tunevault.example/album/the-harbour have
Clipstream - http://www.clipstream.example/user/dorvelquist
Chirpline - https://chirpline.example/Teo_Varsko
Friendwall - https://www.friendwall.example/dorvelquist
For all the wording and info etc… I can email through.
Thank you! Please contact me anytime to get more info or wording, photos etc.. I can send through anything you like to work on the site!
Thanks again,

```html
<!DOCTYPE html>
<html lang="en">
<head>
<meta charset="utf-8">
<title>Teo Varsko — Official Website</title>
<link href="https://fonts.googleapis.com/css2?family=Open+Sans:wght@400;600;700&family=Poiret+One&family=Quicksand:wght@500&display=swap" rel="stylesheet">
<style>
  :root{
    --bg:#141414;
    --ink:#e6e6e6;
    --ink-dim:#6d6d6d;
    --ink-blue:#8a96a6;
    --line:#3c3c3c;
    --nav-top:#262626;
    --nav-bottom:#1a1a1a;
    --accent-red:#c4221c;
    --social-blue:#1f6fc9;
    --social-red:#cc2a22;
    --social-sky:#29a9e8;
    --social-navy:#1c6fbf;
  }
  *{margin:0;padding:0;box-sizing:border-box}
  html,body{width:842px;height:1200px;overflow:hidden;background:var(--bg)}
  body{position:relative;font-family:"Open Sans",Arial,sans-serif;color:var(--ink)}
  .hero-photo{
    position:absolute;inset:0;
    background:
      radial-gradient(ellipse 190px 260px at 420px 520px, rgba(120,120,120,.35), transparent 70%),
      radial-gradient(ellipse 120px 320px at 360px 860px, rgba(60,60,60,.45), transparent 70%),
      radial-gradient(ellipse 420px 600px at 720px 700px, rgba(70,70,70,.25), transparent 70%),
      linear-gradient(180deg,#1b1b1b 0%,#151515 40%,#0e0e0e 100%);
  }
  .site-logo{position:absolute;left:23px;top:88px;font-family:"Quicksand",sans-serif;font-weight:500;font-size:34px;letter-spacing:1.5px;color:#a9a9a9}
  .social{position:absolute;left:650px;top:83px;display:flex;gap:3px}
  .social a{width:40px;height:40px;display:flex;align-items:center;justify-content:center;color:#fff;text-decoration:none;font-size:6.5px;font-weight:600}
  .social .tv{background:var(--social-blue)} .social .cs{background:var(--social-red)}
  .social .cl{background:var(--social-sky)} .social .fw{background:var(--social-navy)}
  .main-nav{position:absolute;left:24px;top:161px;width:793px;height:41px;background:linear-gradient(180deg,var(--nav-top),var(--nav-bottom));border-radius:3px;display:flex;align-items:center}
  .main-nav a{height:41px;display:flex;align-items:center;padding-left:24px;font-size:10.7px;font-weight:700;color:var(--ink-dim);text-decoration:none;border-right:1px solid #111;box-shadow:1px 0 0 #2c2c2c;flex:none}
  .main-nav a.current{color:#d8d8d8}
  .main-nav a:last-child{border:none;box-shadow:none}
  .headline{position:absolute;left:25px;top:236px;font-family:"Poiret One",sans-serif;color:#b0b0b0;font-weight:400}
  .headline .lead{display:block;font-size:32px;line-height:34px}
  .headline .name{display:block;font-size:70px;line-height:60px;letter-spacing:1px}
  .store-badge{position:absolute;left:550px;top:244px;width:267px;height:97px;border:2px solid #c9c9c9;border-radius:10px;background:#000;display:flex;align-items:center;justify-content:center;font-size:34px;font-weight:600;color:#f2f2f2;text-decoration:none}
  .store-note{position:absolute;left:552px;top:356px;width:260px;font-size:10.5px;line-height:15px;color:var(--ink-blue)}
  .video{position:absolute;left:23px;top:430px;width:474px;height:269px;border:1px solid var(--line);background:rgba(10,10,10,.35)}
  .video .play{position:absolute;left:191px;top:81px;width:82px;height:82px;border-radius:50%;background:rgba(40,40,40,.85)}
  .video .progress{position:absolute;left:0;right:0;bottom:24px;height:3px;background:#555}
  .video .progress i{display:block;width:142px;height:3px;background:var(--accent-red)}
  .video .controls{position:absolute;left:0;right:0;bottom:0;height:24px;background:#141414;display:flex;align-items:center;font-family:Arial,sans-serif;font-size:9px;color:#ddd}
  .controls .cell{height:24px;display:flex;align-items:center;justify-content:center;border-right:1px solid #2a2a2a}
  .card{position:absolute;border:1px solid var(--line);background:rgba(8,8,8,.35);padding:33px 32px 0 31px}
  .card h2{font-size:17px;font-weight:400;color:#e9e9e9;line-height:22px}
  .card time{display:block;margin-top:4px;font-size:8.3px;font-weight:700;color:#555;letter-spacing:.3px}
  .card p{margin-top:15px;font-size:10.7px;line-height:20.6px;color:var(--ink-dim)}
  .card .more{position:absolute;left:32px;bottom:31px;font-size:10.7px;font-weight:700;color:#aaa;text-decoration:none}
  .card-a{left:549px;top:430px;width:268px;height:269px}
  .card-b{left:23px;top:752px;width:474px;height:269px;padding-right:52px}
  .card-c{left:549px;top:752px;width:268px;height:269px}
  .site-footer{position:absolute;left:24px;top:1082px;font-size:10.7px;color:var(--ink-dim)}
  .site-footer .row{display:flex;align-items:center;height:18px}
  .site-footer .row+.row{margin-top:23px}
  .site-footer b{font-weight:400;color:#d0d0d0;margin-left:4px}
  .site-footer .sep{width:1px;height:17px;background:#444;margin:0 12px}
  .site-footer a{color:#d0d0d0;text-decoration:none}
  .site-footer .pipe{color:#d0d0d0;margin:0 4px}
</style>
</head>
<body>
  <div class="hero-photo" role="img" aria-label="Moody black and white photograph of the guitarist seated with an electric guitar"></div>

  <div class="site-logo">dorvelquist . com</div>

  <nav class="social" aria-label="Social links">
    <a class="tv" href="https://tunevault.example/album/the-harbour">Tunevault</a>
    <a class="cs" href="http://www.clipstream.example/user/dorvelquist">Clipstream</a>
    <a class="cl" href="https://chirpline.example/Teo_Varsko">Chirpline</a>
    <a class="fw" href="https://www.friendwall.example/dorvelquist">Friendwall</a>
  </nav>

  <nav class="main-nav">
    <a class="current" href="#" style="width:78px">Home</a>
    <a href="#" style="width:78px">News</a>
    <a href="#" style="width:78px">Tours</a>
    <a href="#" style="width:64px">Bio</a>
    <a href="#" style="width:76px">Store</a>
    <a href="#" style="width:73px">Gear</a>
    <a href="#" style="width:76px">Video</a>
    <a href="#">Contact</a>
  </nav>

  <h1 class="headline"><span class="lead">The Official website of</span><span class="name">Teo Varsko</span></h1>

  <a class="store-badge" href="https://tunevault.example/album/the-harbour">Tunevault</a>
  <p class="store-note">Lorem ipsum dolor sit amet, meis vituperatoribus est ut, ex est rebum iudicabit dissentiunt.</p>

  <div class="video">
    <div class="play">
      <svg width="82" height="82" viewBox="0 0 82 82"><path d="M30 24 L58 41 L30 58 Z" fill="#4a4a4a"/></svg>
    </div>
    <div class="progress"><i></i></div>
    <div class="controls">
      <span class="cell" style="width:48px">
        <svg width="10" height="11"><rect x="0" y="0" width="3.5" height="11" fill="#bbb"/><rect x="6.5" y="0" width="3.5" height="11" fill="#bbb"/></svg>
      </span>
      <span class="cell" style="width:34px">
        <svg width="18" height="12"><path d="M0 4h3l4-4v12l-4-4H0z" fill="#8fb4e0"/><path d="M10 3q2 3 0 6M13 1q4 5 0 10" stroke="#8fb4e0" fill="none"/></svg>
      </span>
      <span style="padding-left:4px">0:05 <span style="color:#999">/ 0:24</span></span>
      <span style="margin-left:auto;display:flex;align-items:center">
        <svg width="12" height="10" style="margin-right:14px"><rect width="12" height="8" fill="#b02520"/><path d="M3 8l0 2 3-2z" fill="#b02520"/></svg>
        <span style="color:#bbb;margin-right:6px">360p</span>
      </span>
      <span class="cell" style="width:24px;border-left:1px solid #2a2a2a">
        <svg width="12" height="10"><path d="M1 3h9l-2-2M11 7H2l2 2" stroke="#aaa" fill="none"/></svg>
      </span>
      <span class="cell" style="width:26px;border-right:none">
        <svg width="11" height="11"><path d="M0 3V0h3M8 0h3v3M11 8v3H8M3 11H0V8" stroke="#aaa" fill="none"/></svg>
      </span>
    </div>
  </div>

  <article class="card card-a">
    <h2>Title Goes Here</h2>
    <time>12 MAR 2014</time>
    <p>Lorem ipsum dolor sit amet, meis vituperatoribus est ut, ex est rebum iudicabit dissentiunt. Mel ne elitr atomorum, vix ad agam aliquip evertitur, cum omnesque tractatos cu. Cu pri</p>
    <a class="more" href="#">Read more</a>
  </article>

  <article class="card card-b">
    <h2>Title Goes Here</h2>
    <time>12 MAR 2014</time>
    <p>Lorem ipsum dolor sit amet, meis vituperatoribus est ut, ex est rebum iudicabit dissentiunt. Mel ne elitr atomorum, vix ad agam aliquip evertitur, cum omnesque tractatos cu. Cu pri propriae atomorum, te dicta quando eam. An eos putant aeterno, repudiare appellantur conclusionemque per id. Eu cum dicant intellegat.</p>
    <a class="more" href="#">Read more</a>
  </article>

  <article class="card card-c">
    <h2>Title Goes Here</h2>
    <time>12 MAR 2014</time>
    <p>Lorem ipsum dolor sit amet, meis vituperatoribus est ut, ex est rebum iudicabit dissentiunt. Mel ne elitr atomorum, vix ad agam aliquip evertitur, cum omnesque tractatos cu. Cu pri</p>
    <a class="more" href="#">Read more</a>
  </article>

  <footer class="site-footer">
    <div class="row">Management: <b>Name Surname &amp; Company Name</b><span class="sep"></span>Booking inquiries: <b>Name Surname / Company Name</b></div>
    <div class="row">© 2014 dorvelquist.com. All Rights Reserved.<span class="sep"></span><a href="#">Press Information</a><span class="pipe">|</span><a href="#">Contact</a><span class="pipe">|</span><a href="#">Credits</a></div>
  </footer>
</body>
</html>
```